Velmora Outcomes Brochure Design Project

- Who we are?
Velmora Outcomes is New Internet Marketing Company Based in China.

It is our aim to provide Chinese clients with the means to internationally market their product, via the Internet.

Our primary products are Outsourced Design ( Thanks to Pixel hive and the amazing designers who use it), SEO and Virtual Hosting.

- Project Brief
Design a vibrant and fresh brochure that introduces the fundamentals of SEO. There is no restriction to the number of pages, however all the info I have included in this brief must be included.

- Colour Palette
Please see link or download the Adobe Swatch Exchange File or follow the link below
http://tintaro.example.com/#themes/search?term=5830716
Updates

Logo updated - grey background removed

Various file formats added for logo and brochure content

Brochure zip file add containing logo in different formats.

Adobe color scheme file added

The general corporate colors are:

Base Color: CMYK :0, 60, 80, 0  Hex: FF6633
Dark Orange: CMYK: 0, 72, 96, 30 Hex: B23308
Light Orange: CMYK 0, 42, 56, 0 Hex: FF9571
Grey: CMYK 0, 0, 0, 48 Hex: 858585
Light Grey: CMYK 0, 0, 0, 26 Hex: BDBDBD

Please note that I'm happy for other colors to be included, however I would like these the corporate branding colors to be clearly present through the brochure.

Hi All

First place payment has increased to $600 - Looking to see some creative designs!

Hi All

Project Deadline Extended
Reason: I have increase the budget and extend the deadline as I need to see more design.

I have attached a zip file that contains example brochures I like.

We are not keen on the table data its a little plain. We have create an info-graphic to replace one of the table and would like to see it included in the design.

Project Deadline Extended
Reason: A few designers have asked for this extension and I would like to see additional designs. Thanks Marek

Target Market(s)

- Our Target Audience is..
It is small to medium businesses looking to reach out to the international market.
Our clients still very much operate on a face to face level in business and are new to the concept of Internet marketing

However this must look professional, Marketable and Clean, with the power of connecting people globally, through SEO and design to be reflected visually in the brochure.

Industry/Entity Type

Internet

Requirements
Must have
• One or more of the FACTS that I have highlighted need to stand out on each page. These FACTS can be found the document attached to this brief and are under the section titled 'Did You Know!'. Not every fact in this section needs to be highlighted in the brochure, but each page needs to have at least, one or more fact that stands out, soemwhere on the page.
See attached document, under the heading 'Did you Know!' and use one or two of these facts to spruce up the pages!

One image/ per page or per two pages MUST be included!

- Provide stock photos and please send us a message with the additional cost of these with your submission

The Table data, that I have included in the attachment must be included in the body of the pages - BUT the table format is not necessary and you can place the information in the body like plain text.

The brochure size should be a little larger than A4.

Please design the back page, like a pocket to hold paper and other material in it that I include with this brochure.

```html
<!DOCTYPE html>
<html lang="en">
<head>
<meta charset="utf-8">
<title>Velmora Outcomes Brochure – Contents Spread</title>
<link rel="stylesheet" href="https://fonts.googleapis.com/css2?family=Oswald:wght@500;600&family=Titillium+Web:wght@300;400;600&display=swap">
<style>
  :root {
    --stage: #000000;
    --orange: #f0834c;
    --orange-bright: #f2874d;
    --ink: #1b1310;
    --rule: #8a3f1c;
    --white: #ffffff;
    --photo-light: #e9e6e4;
    --photo-mid: #c9a888;
    --photo-dark: #3a2a24;
  }
  * { margin: 0; padding: 0; box-sizing: border-box; }
  html, body {
    width: 1200px;
    height: 900px;
    overflow: hidden;
    background: var(--stage);
  }
  .canvas {
    position: relative;
    width: 1200px;
    height: 900px;
    background: var(--stage);
    font-family: "Titillium Web", Arial, sans-serif;
  }
  .spread {
    position: absolute;
    left: 30px;
    top: 113px;
    width: 1140px;
    height: 677px;
    overflow: hidden;
  }
  .page-contents {
    position: absolute;
    left: 0;
    top: 0;
    width: 570px;
    height: 677px;
    background: var(--orange);
  }
  .page-feature {
    position: absolute;
    left: 570px;
    top: 0;
    width: 570px;
    height: 677px;
    overflow: hidden;
  }
  .feature-photo {
    position: absolute;
    inset: 0;
    background:
      radial-gradient(ellipse at 20% 35%, var(--photo-mid) 0%, transparent 40%),
      radial-gradient(ellipse at 55% 75%, var(--photo-mid) 0%, transparent 45%),
      radial-gradient(ellipse at 85% 60%, #d9b995 0%, transparent 35%),
      linear-gradient(160deg, var(--photo-light) 0%, #bdb5b2 30%, var(--photo-dark) 70%, #241a17 100%);
  }
  .feature-title {
    position: absolute;
    left: 1034px;
    top: 320px;
    transform: translate(-50%, -50%) rotate(-90deg) scaleX(0.83);
    font-family: "Oswald", "Arial Narrow", sans-serif;
    font-weight: 500;
    font-size: 198px;
    line-height: 1;
    letter-spacing: 6px;
    color: var(--orange-bright);
    white-space: nowrap;
  }
  .diagram {
    position: absolute;
    left: 0;
    top: 0;
    width: 1200px;
    height: 900px;
  }
  .hub-label {
    position: absolute;
    left: 160px;
    top: 533px;
    width: 118px;
    text-align: center;
    font-family: "Oswald", "Arial Narrow", sans-serif;
    font-weight: 600;
    font-size: 31px;
    line-height: 40px;
    color: var(--white);
  }
  .topic {
    position: absolute;
    color: var(--ink);
  }
  .topic-title {
    font-size: 15px;
    font-weight: 300;
    line-height: 16px;
    letter-spacing: 0.3px;
    color: var(--white);
    text-transform: uppercase;
  }
  .topic-text {
    font-size: 9.6px;
    line-height: 11.6px;
    font-weight: 400;
  }
  .topic-pages {
    font-size: 9.6px;
    line-height: 12px;
    font-weight: 600;
    margin-top: 1px;
  }
  .topic-seo { left: 227px; top: 203px; }
  .topic-web { left: 441px; top: 403px; }
  .topic-blog { left: 74px; top: 634px; }
  .topic-logo { left: 349px; top: 661px; }
</style>
</head>
<body>
<main class="canvas">
  <section class="spread">
    <div class="page-contents"></div>
    <div class="page-feature">
      <div class="feature-photo" role="img" aria-label="Close-up photograph of a bundle of sharpened coloured pencils with red, black, blue and green tips"></div>
    </div>
  </section>

  <svg class="diagram" viewBox="0 0 1200 900" aria-hidden="true">
    <defs>
      <marker id="arrowhead" viewBox="0 0 6 6" refX="5" refY="3" markerWidth="6" markerHeight="6" orient="auto">
        <path d="M0 0 L6 3 L0 6 Z" fill="var(--rule)"/>
      </marker>
    </defs>
    <g stroke="var(--rule)" stroke-width="1" fill="none">
      <line x1="219" y1="485" x2="219" y2="214" marker-end="url(#arrowhead)"/>
      <line x1="278" y1="517" x2="434" y2="423" marker-end="url(#arrowhead)"/>
      <line x1="162" y1="590" x2="96" y2="628" marker-end="url(#arrowhead)"/>
      <line x1="276" y1="588" x2="364" y2="654" marker-end="url(#arrowhead)"/>
    </g>
    <polygon class="hub" points="219,485 278,519 278,588 219,622 160,588 160,519" fill="var(--orange-bright)"/>
  </svg>

  <div class="hub-label">CONTENT</div>

  <div class="topic topic-seo">
    <div class="topic-title">SEO</div>
    <p class="topic-text">Ibus adis ad Ceptamus<br>as accabo. Et aut odi con<br>nonsed qui debis porerior<br>resti bla dempore voloreh<br>endant a venditi untur</p>
    <p class="topic-pages">Page 8-14</p>
  </div>

  <div class="topic topic-web">
    <div class="topic-title">Web Design</div>
    <p class="topic-text">Ibus adis Est exernatu-<br>rita imint laut ullique pro<br>es Eque optis nos qui de-<br>pra cus simporit volorro<br>ipictur molore re.</p>
    <p class="topic-pages">Page 15-21</p>
  </div>

  <div class="topic topic-blog">
    <div class="topic-title">Blog</div>
    <p class="topic-text">At que vellorem nimust modisi<br>officte Ullorerum quid magnihi<br>llabo. Ro beatur si si blatatem.</p>
    <p class="topic-pages">Page 22-23</p>
  </div>

  <div class="topic topic-logo">
    <div class="topic-title">Logo Design</div>
    <p class="topic-text">Ibus a Luptus magnihitas de<br>expla sa volo volum qui derionse-<br>qui unt qui quia audis ulloratem<br>labor sequaec turiae assequaero</p>
    <p class="topic-pages">Page 3-7</p>
  </div>

  <div class="feature-title">LOGO</div>
</main>
</body>
</html>
```